Technology management company looking for a new website with a professional look

Brennick IT is a recently re-branded technology management company that is looking for a website design to match its personalized approach and friendly culture.

We would like to see a specialized, but related, page style for each of our main service offerings of:

• Commercial IT Support (This is our primary focus)
• Commercial Phone Systems (We partner with http://www.voxtrell.com/ for our phone systems)
• Point of Sale Systems (We partner with http://www.tillmora.com/ for our POS systems.
• Web Design
• Hollow Pine Computers (Our residential computer service offering, branded as Hollow Pine Computers)

The Hollow Pine Computers page should be build upon the Hollow Pine Computers logo, the other four pages should be branded as Brennick IT.

These five separate pages should have subtle, yet clearly defined links to one another. They should also each have a Home, Products, Service, and Company in the menu.

The website should have a clean design with professional appeal, but not appear too sterile or uninviting. It needs to have a simple, easy to navigate menu interface along the top. We would also like the site to be mobile friendly.

It should also allow us to easily tie in links to our social media pages (Friendbook, Linkwise, Chirper and Circles+) and provide easy access to our contact information from each page.

This is a link to our old website www.hollowpinecomputers.com

We don't currently have copy available. The text and menu design should be easily editable and expandable so we can use the design to fit our copy.

In general we are looking for a concept we can modify to fit our needs.

We need this design to be available with layers in a .psd format.

Target Market(s)

Small to mid-size businesses.

Industry/Entity Type

Information Technology

Number of Pages Required

5+ page

Font styles to use
Sans Serif

Requirements
Must have
• Mobile Friendly
• Professional Type Face
• Unity between all pages
• .PSD Format
Nice to have
• Themed with our logo
Should not have
• Bubbly unprofessional typeface. No comic sans.

```html
<!DOCTYPE html>
<html lang="en">
<head>
<meta charset="utf-8">
<title>Brennick IT</title>
<link href="https://fonts.googleapis.com/css2?family=Open+Sans:wght@400;600;700;800&display=swap" rel="stylesheet">
<style>
:root{
  --orange:#f26522;
  --blue:#1f5fa6;
  --blue-dark:#163f73;
  --ink:#111417;
  --night:#0a1a33;
  --grey:#6d6d6d;
  --light:#f4f4f4;
  --white:#ffffff;
}
*{box-sizing:border-box;margin:0;padding:0}
html,body{width:1200px;height:2208px;overflow:hidden}
body{font-family:'Open Sans',Arial,sans-serif;background:var(--white);color:var(--grey);position:relative}
.topbar{height:88px;display:flex;align-items:center;justify-content:space-between;padding:0 80px}
.brand{display:flex;align-items:center;gap:14px}
.brand-dot{width:40px;height:40px;border-radius:50%;background:var(--orange)}
.brand-name{font-size:44px;font-weight:700;color:var(--blue-dark);letter-spacing:-1px}
.contact-mini{display:flex;gap:34px;font-size:16px;color:#333}
.contact-mini span{display:flex;align-items:center;gap:8px}
.contact-mini i{width:26px;height:26px;border-radius:50%;background:var(--orange);display:inline-flex;align-items:center;justify-content:center}
.nav{height:40px;background:var(--ink);display:flex;padding-left:80px}
.nav a{color:var(--white);font-size:13px;text-decoration:none;padding:0 14px;line-height:40px;text-transform:uppercase}
.nav a.active{background:var(--orange);width:46px;padding:0}
.hero{position:relative;height:360px;background:linear-gradient(90deg,#040b18 0%,#0a1a33 45%,#0f2b55 100%);overflow:hidden}
.hero-art{position:absolute;right:0;top:0;width:660px;height:360px;background:radial-gradient(circle at 55% 50%,#3c7bc4 0%,#163a6e 45%,rgba(10,26,51,0) 80%)}
.hero-copy{position:absolute;left:80px;top:56px;width:440px}
.hero-copy h1{font-weight:600;font-size:44px;line-height:46px;color:var(--white);text-transform:uppercase}
.hero-copy h1 .o{color:var(--orange)}
.hero-copy h1 .b{color:#4fa3ff}
.hero-copy p{margin-top:18px;font-size:13px;line-height:19px;color:var(--orange)}
.btn-outline{display:inline-block;margin-top:22px;border:1px solid var(--orange);color:var(--white);font-size:12px;padding:8px 26px;text-transform:uppercase}
.section-title{text-align:center;font-size:36px;font-weight:400;color:var(--blue);text-transform:uppercase}
.section-title::after{content:"";display:block;width:60px;height:2px;background:var(--blue);margin:12px auto 0}
.services{position:absolute;top:690px;left:0;width:1200px}
.service-row{display:flex;justify-content:center;gap:30px;margin-top:50px}
.service{width:198px;text-align:center}
.service svg{display:block;margin:0 auto}
.service h3{margin-top:24px;font-size:20px;line-height:24px;font-weight:600;color:var(--orange);text-transform:uppercase;height:48px}
.service p{margin-top:18px;font-size:12px;line-height:17px;color:#555;height:85px}
.btn-small{display:inline-block;margin-top:14px;border:1px solid var(--orange);color:var(--blue);font-size:11px;padding:6px 20px;text-transform:uppercase}
.why{position:absolute;top:1250px;left:0;width:1200px;height:470px;background:linear-gradient(180deg,#1d5ea8,#174f91)}
.why-copy{position:absolute;left:80px;top:40px;width:560px;color:var(--white)}
.why-copy h2{font-size:36px;font-weight:400;color:var(--orange);text-transform:uppercase}
.why-copy p{margin-top:22px;font-size:12px;line-height:17px}
.why-copy h4{margin-top:22px;font-size:14px;font-weight:600;color:var(--orange);text-transform:uppercase}
.why-list{margin-top:16px;display:grid;grid-template-columns:1fr 1fr;row-gap:10px;list-style:none;font-size:12px}
.why-list li::before{content:"";display:inline-block;width:6px;height:6px;border-radius:50%;background:var(--white);margin-right:10px;vertical-align:middle}
.why-art{position:absolute;right:80px;top:40px;width:400px;height:380px;background:radial-gradient(circle at 50% 55%,#e9eef5 0%,#8fb3dc 45%,rgba(23,79,145,0) 75%)}
.partners{position:absolute;top:1760px;left:0;width:1200px}
.partner-row{display:flex;align-items:center;justify-content:center;gap:24px;margin-top:30px}
.arrow{width:24px;height:24px;border-radius:50%;background:#ddd;display:flex;align-items:center;justify-content:center}
.partner-badge{width:170px;height:100px;background:var(--white);border:1px solid #ddd;box-shadow:0 2px 6px rgba(0,0,0,.12);display:flex;align-items:center;justify-content:center}
.partner-badge i{width:90px;height:26px;background:#e2e2e2;border-radius:3px}
.footer{position:absolute;top:1950px;left:0;width:1200px;height:242px;background:var(--ink);display:flex;padding:22px 80px 0;gap:30px;color:#ccc}
.footer h5{font-size:12px;color:var(--white);text-transform:uppercase;font-weight:600;border-bottom:1px solid #333;padding-bottom:8px;margin-bottom:10px}
.footer ul{list-style:none;font-size:11px;line-height:20px}
.f-col{width:220px}
.f-news{width:300px}
.f-news p{font-size:11px;line-height:16px}
.field{margin-top:10px;height:22px;width:260px;background:var(--white)}
.f-btn{margin-top:8px;display:inline-block;background:var(--orange);color:var(--white);font-size:11px;padding:4px 16px}
.social li{display:flex;align-items:center;gap:8px;margin-bottom:4px}
.social li i{width:14px;height:14px;background:var(--orange)}
.copyright{position:absolute;top:2192px;left:0;width:1200px;height:16px;background:var(--night);font-size:8px;color:#889;text-align:center;line-height:16px}
</style>
</head>
<body>
<header class="topbar">
  <div class="brand"><span class="brand-dot"></span><span class="brand-name">Brennick IT</span></div>
  <div class="contact-mini">
    <span><i><svg width="14" height="10" viewBox="0 0 14 10"><rect x="0.5" y="0.5" width="13" height="9" fill="none" stroke="#fff"/><path d="M1 1l6 5 6-5" fill="none" stroke="#fff"/></svg></i>info@brennickit.com</span>
    <span><i><svg width="12" height="12" viewBox="0 0 12 12"><path d="M2 1l3 0 1 3-2 1a7 7 0 0 0 3 3l1-2 3 1 0 3c-6 0-9-3-9-9z" fill="#fff"/></svg></i>555 010 4477</span>
  </div>
</header>
<nav class="nav">
  <a class="active" href="#"></a>
  <a href="#">Commercial IT Support</a>
  <a href="#">Commercial Phone Systems</a>
  <a href="#">Point of Sale Systems</a>
  <a href="#">Web Design</a>
  <a href="#">Hollow Pine Computers</a>
  <a href="#">Contact</a>
</nav>
<section class="hero">
  <div class="hero-art" role="img" aria-label="Hand touching glowing technology icons on a dark blue background"></div>
  <div class="hero-copy">
    <h1><span class="o">We are</span><br><span class="b">IT Management</span><br>Company</h1>
    <p>Commercial IT Support, Commercial Phone Systems, Point of Sale Systems, Web Design. Brennick IT helps growing businesses work smarter with friendly, personal service and reliable technology.</p>
    <span class="btn-outline">Learn more about Brennick IT</span>
  </div>
</section>
<section class="services">
  <h2 class="section-title">Services</h2>
  <div class="service-row">
    <div class="service">
      <svg width="160" height="160" viewBox="0 0 160 160" role="img" aria-label="Commercial IT support icon"><circle cx="80" cy="80" r="72" fill="none" stroke="#f26522" stroke-width="12"/><path d="M8 80a72 72 0 0 1 144 0" fill="none" stroke="#1f5fa6" stroke-width="12"/><circle cx="80" cy="80" r="54" fill="#f4f4f4"/></svg>
      <h3>Commercial<br>IT Support</h3>
      <p>Proactive monitoring, help desk support and network care that keeps every workstation in your office running smoothly all year.</p>
      <span class="btn-small">Learn more</span>
    </div>
    <div class="service">
      <svg width="160" height="160" viewBox="0 0 160 160" role="img" aria-label="Commercial phone systems icon"><circle cx="80" cy="80" r="72" fill="none" stroke="#f26522" stroke-width="12"/><path d="M8 80a72 72 0 0 1 144 0" fill="none" stroke="#1f5fa6" stroke-width="12"/><circle cx="80" cy="80" r="54" fill="#f4f4f4"/></svg>
      <h3>Commercial<br>Phone Systems</h3>
      <p>Modern office phone systems with clear calls, easy voicemail and flexible lines that grow along with your team and business.</p>
      <span class="btn-small">Learn more</span>
    </div>
    <div class="service">
      <svg width="160" height="160" viewBox="0 0 160 160" role="img" aria-label="Point of sale systems icon"><circle cx="80" cy="80" r="72" fill="none" stroke="#f26522" stroke-width="12"/><path d="M8 80a72 72 0 0 1 144 0" fill="none" stroke="#1f5fa6" stroke-width="12"/><circle cx="80" cy="80" r="54" fill="#f4f4f4"/></svg>
      <h3>Point of<br>Sale Systems</h3>
      <p>Fast, dependable checkout stations and inventory tools set up for retail shops and restaurants with ongoing local support.</p>
      <span class="btn-small">Learn more</span>
    </div>
    <div class="service">
      <svg width="160" height="160" viewBox="0 0 160 160" role="img" aria-label="Web design icon"><circle cx="80" cy="80" r="72" fill="none" stroke="#f26522" stroke-width="12"/><path d="M8 80a72 72 0 0 1 144 0" fill="none" stroke="#1f5fa6" stroke-width="12"/><circle cx="80" cy="80" r="54" fill="#f4f4f4"/></svg>
      <h3>Web Design</h3>
      <p>Clean, mobile friendly websites that present your business well and make it simple for customers to reach you.</p>
      <span class="btn-small">Learn more</span>
    </div>
    <div class="service">
      <svg width="160" height="160" viewBox="0 0 160 160" role="img" aria-label="Residential computer service icon"><circle cx="80" cy="80" r="72" fill="none" stroke="#f26522" stroke-width="12"/><path d="M8 80a72 72 0 0 1 144 0" fill="none" stroke="#1f5fa6" stroke-width="12"/><circle cx="80" cy="80" r="54" fill="#f4f4f4"/></svg>
      <h3>Hollow Pine<br>Computers</h3>
      <p>Friendly home computer repair, virus removal and upgrades for families, delivered by the same trusted local team.</p>
      <span class="btn-small">Learn more</span>
    </div>
  </div>
</section>
<section class="why">
  <div class="why-copy">
    <h2>Why choose us?</h2>
    <p>We believe technology should make work easier, not harder. Our team takes the time to learn how your business runs, then builds and supports systems that fit. You get one local partner for computers, phones, point of sale and web, with clear pricing and quick, friendly answers whenever you call.</p>
    <h4>Our industry-sector experience includes:</h4>
    <ul class="why-list">
      <li>Retail stores and shops</li><li>Medical and dental offices</li>
      <li>Restaurants and cafes</li><li>Legal and accounting firms</li>
      <li>Manufacturing companies</li><li>Schools and nonprofits</li>
      <li>Real estate agencies</li><li>Home and family users</li>
    </ul>
  </div>
  <div class="why-art" role="img" aria-label="Stack of colourful 3D cubes"></div>
</section>
<section class="partners">
  <h2 class="section-title">Our Partners</h2>
  <div class="partner-row">
    <span class="arrow"><svg width="10" height="10" viewBox="0 0 10 10"><path d="M7 1L3 5l4 4" fill="none" stroke="#555" stroke-width="1.5"/></svg></span>
    <div class="partner-badge"><i></i></div>
    <div class="partner-badge"><i></i></div>
    <div class="partner-badge"><i></i></div>
    <div class="partner-badge"><i></i></div>
    <div class="partner-badge"><i></i></div>
    <span class="arrow"><svg width="10" height="10" viewBox="0 0 10 10"><path d="M3 1l4 4-4 4" fill="none" stroke="#555" stroke-width="1.5"/></svg></span>
  </div>
</section>
<footer class="footer">
  <div class="f-col">
    <h5>Quick Links</h5>
    <ul><li>› Home</li><li>› Commercial IT Support</li><li>› Commercial Phone Systems</li><li>› Point of Sale Systems</li><li>› Web Design</li><li>› Hollow Pine Computers</li><li>› Contact</li></ul>
  </div>
  <div class="f-col">
    <h5>Contact Information</h5>
    <ul><li>12 Harbor Lane, Suite 4</li><li>Millbrook, ST 00000</li><li>+1 (555) 010 4477</li><li>info@brennickit.com</li></ul>
  </div>
  <div class="f-news">
    <h5>Newsletter Signup</h5>
    <p>Enter your email below to receive our latest news and helpful tips.</p>
    <div class="field"></div>
    <span class="f-btn">Submit</span>
  </div>
  <div class="f-col">
    <h5>Follow Us</h5>
    <ul class="social"><li><i></i>Friendbook</li><li><i></i>Linkwise</li><li><i></i>Chirper</li><li><i></i>Circles+</li><li><i></i>Feed</li></ul>
  </div>
</footer>
<div class="copyright">Copyright © Brennick IT. All rights reserved.</div>
</body>
</html>
```